Bref créative
Business Cards & Stationary For Law Firm - Use Existing Logo
Harlow Law Offices
I need double sided standard sized Business Card [3.5" x 2"]
I am open to different fonts for the info. I have used Century Gothic before but try any
Professional
Dorian P. Harlow, Esq.
482 N.E. 3rd Avenue
Suite 2206
Bayview, Florida 33190
dph@harlowlo.example
www.harlowlo.example
To me the most important thing on a card is that they get your information quickly and easily. I see so many cards that are unmemorable and cluttered with tiny type. I think people want your name and phone easy to read and accessible.
Can put logo and/or any information on either side. Try different designs.

```html
<!DOCTYPE html>
<html lang="en">
<head>
<meta charset="utf-8">
<title>Harlow Law Offices — Business Card</title>
<link rel="stylesheet" href="https://fonts.googleapis.com/css2?family=Cinzel:wght@400;600&display=swap">
<style>
  :root {
    --backdrop: #e9e6e1;
    --card-white: #ffffff;
    --navy: #1b2f66;
    --brand-blue: #2b55c4;
    --band-light: #3a6ee0;
    --band-dark: #1d3d9c;
    --rule-dark: #1c1f2a;
    --ink-light: #ffffff;
  }
  * { margin: 0; padding: 0; box-sizing: border-box; }
  html, body { width: 1200px; height: 902px; overflow: hidden; }
  body { background: var(--backdrop); position: relative; font-family: "Cinzel", serif; }

  .business-card {
    position: absolute; left: 100px; top: 165px;
    width: 1000px; height: 572px;
    background: var(--card-white);
    box-shadow: 0 6px 18px rgba(0,0,0,0.18);
    overflow: hidden;
  }

  .brand {
    position: absolute; left: 255px; top: 78px;
    display: flex; align-items: center; gap: 26px;
  }
  .brand-square { width: 74px; height: 74px; background: var(--navy); }
  .brand-divider { width: 2px; height: 96px; background: var(--navy); }
  .brand-name { color: var(--navy); font-weight: 400; line-height: 1; }
  .brand-name .firm { display: block; font-size: 62px; letter-spacing: 2px; }
  .brand-name .practice { display: block; font-size: 22px; letter-spacing: 6px; margin-top: 6px; }

  .info-band {
    position: absolute; left: 0; top: 262px; width: 100%; height: 310px;
    background: linear-gradient(180deg, var(--band-light) 0%, var(--brand-blue) 45%, var(--band-dark) 100%);
  }
  .band-rule {
    position: absolute; left: 0; top: 250px; width: 440px; height: 14px;
    background: var(--rule-dark);
  }
  .band-notch { position: absolute; left: 38px; top: 263px; }

  .attorney-name {
    position: absolute; left: 42px; top: 310px;
    color: var(--ink-light); font-size: 22px; letter-spacing: 1px;
  }

  .contact-list {
    position: absolute; left: 600px; top: 288px; list-style: none;
    color: var(--ink-light); font-size: 15px; letter-spacing: 0.5px;
  }
  .contact-list li { display: flex; align-items: center; gap: 10px; height: 21px; white-space: nowrap; }
  .contact-list svg { width: 14px; height: 14px; flex: none; }
</style>
</head>
<body>
  <div class="business-card">
    <div class="brand">
      <div class="brand-square"></div>
      <div class="brand-divider"></div>
      <div class="brand-name">
        <span class="firm">HARLOW</span>
        <span class="practice">LAW OFFICES</span>
      </div>
    </div>

    <div class="info-band"></div>
    <div class="band-rule"></div>
    <svg class="band-notch" width="24" height="14" viewBox="0 0 24 14"><polygon points="0,0 24,0 6,14" fill="var(--rule-dark)"/></svg>

    <p class="attorney-name">Dorian P. Harlow, Esq.</p>

    <ul class="contact-list">
      <li><svg viewBox="0 0 14 14"><circle cx="7" cy="7" r="7" fill="#fff"/><path d="M7 3a2.5 2.5 0 0 0-2.5 2.5C4.5 8 7 11 7 11s2.5-3 2.5-5.5A2.5 2.5 0 0 0 7 3z" fill="var(--brand-blue)"/></svg>482 N.E. 3rd Avenue Suite 2206</li>
      <li><svg viewBox="0 0 14 14"></svg>Bayview, Florida 33190</li>
      <li><svg viewBox="0 0 14 14"><circle cx="7" cy="7" r="7" fill="#fff"/><path d="M4.5 3.5l2 2-1 1a5 5 0 0 0 2 2l1-1 2 2-1.2 1.2C6.5 10.5 3.5 7.5 3.3 4.7z" fill="var(--brand-blue)"/></svg>786-555-0142</li>
      <li><svg viewBox="0 0 14 14"><circle cx="7" cy="7" r="7" fill="#fff"/><rect x="4" y="5" width="6" height="4" fill="var(--brand-blue)"/></svg>786-555-0187</li>
      <li><svg viewBox="0 0 14 14"><circle cx="7" cy="7" r="7" fill="#fff"/><rect x="3.5" y="4.5" width="7" height="5" fill="none" stroke="var(--brand-blue)"/><path d="M3.5 4.5L7 7.5l3.5-3" fill="none" stroke="var(--brand-blue)"/></svg>dph@harlowlo.example</li>
      <li><svg viewBox="0 0 14 14"><circle cx="7" cy="7" r="7" fill="#fff"/><circle cx="7" cy="7" r="3.5" fill="none" stroke="var(--brand-blue)"/><path d="M3.5 7h7M7 3.5v7" stroke="var(--brand-blue)"/></svg>www.harlowlo.example</li>
    </ul>
  </div>
</body>
</html>
```